Business Card Design

We have our logo and everything in place. Looking to have a layout for our new business cards designed. These will be printed with a matte finish, possibly rounded corners, and looking to incorporate some cool spot UV layers into the design.

Ive uploaded the existing card front and back as well as our logo.

Card Size Will Be 3.5" x 2"

Industry/Entity Type

Business

```html
<!DOCTYPE html>
<html lang="en">
<head>
<meta charset="utf-8">
<title>Ridgeline Deck and Rail – Business Cards</title>
<link href="https://fonts.googleapis.com/css2?family=Old+Standard+TT:wght@400&display=swap" rel="stylesheet">
<style>
  :root {
    --backdrop: #3b3430;
    --card: #121212;
    --card-edge: #050505;
    --silver: #d9d9d9;
    --silver-dim: #a8a8a8;
    --gloss: #262626;
  }
  * { margin: 0; padding: 0; box-sizing: border-box; }
  html, body { width: 1200px; height: 716px; overflow: hidden; }
  body {
    background: var(--backdrop);
    font-family: "Old Standard TT", Georgia, serif;
    position: relative;
  }
  .card {
    position: absolute;
    width: 490px;
    height: 280px;
    background: var(--card);
    border-radius: 6px;
  }
  .card--front { left: 70px; top: 218px; border: 1px solid var(--card-edge); }
  .card--back { left: 640px; top: 218px; box-shadow: inset 0 0 0 3px var(--silver-dim); }

  .wordmark {
    position: absolute;
    text-align: center;
    font-weight: 400;
    letter-spacing: 2px;
    white-space: nowrap;
  }
  .card--front .wordmark {
    left: 0; right: 0; top: 118px;
    font-size: 30px;
    color: var(--gloss);
  }
  .card--front .wordmark-rule {
    position: absolute;
    left: 95px; right: 95px; top: 166px;
    border-top: 1px solid var(--gloss);
  }

  .card--back .wordmark {
    top: 40px; right: 30px;
    font-size: 24px;
    color: var(--silver);
  }
  .card--back .wordmark-rule {
    position: absolute;
    left: 250px; right: 30px; top: 82px;
    border-top: 1px solid var(--silver-dim);
  }
  .holder {
    position: absolute;
    left: 30px; top: 96px;
    padding-top: 6px;
    border-top: 1px solid var(--silver-dim);
  }
  .holder-name {
    font-size: 20px;
    letter-spacing: 3px;
    color: var(--silver);
    text-transform: uppercase;
  }
  .holder-title {
    font-size: 13px;
    color: var(--silver-dim);
    margin-top: 2px;
  }
  .contacts {
    position: absolute;
    right: 22px; top: 178px;
    list-style: none;
    text-align: right;
  }
  .contacts li {
    font-size: 14px;
    letter-spacing: 1px;
    color: var(--silver);
    line-height: 26px;
    display: flex;
    justify-content: flex-end;
    align-items: center;
    gap: 10px;
  }
  .contacts li.contact-phone { font-size: 15px; }
  .contacts svg { width: 12px; height: 12px; flex: none; }
</style>
</head>
<body>
  <section class="card card--front" aria-label="Card front">
    <div class="wordmark">Ridgeline Deck and Rail</div>
    <div class="wordmark-rule"></div>
  </section>

  <section class="card card--back" aria-label="Card back">
    <div class="wordmark">Ridgeline Deck and Rail</div>
    <div class="wordmark-rule"></div>
    <div class="holder">
      <div class="holder-name">Daniel Morrow</div>
      <div class="holder-title">President</div>
    </div>
    <ul class="contacts">
      <li class="contact-phone">403.555.0187
        <svg viewBox="0 0 12 12"><rect width="12" height="12" rx="1" fill="#d9d9d9"/><path d="M4 3c-.8.6-.8 1.8 0 3s2.2 2.6 3.2 2.9c.7.2 1.2-.1 1.5-.6L7.6 7.2 6.8 7.7C6.2 7.3 5 6 4.7 5.3l.6-.8L4.3 3z" fill="#121212"/></svg>
      </li>
      <li class="contact-email">hello@ridgelinedeckandrail.com
        <svg viewBox="0 0 12 12"><rect width="12" height="12" rx="1" fill="#d9d9d9"/><rect x="2.5" y="3.5" width="7" height="5" fill="none" stroke="#121212"/><path d="M2.5 3.5 6 6.5 9.5 3.5" fill="none" stroke="#121212"/></svg>
      </li>
      <li class="contact-web">www.ridgelinedeckandrail.com
        <svg viewBox="0 0 12 12"><rect width="12" height="12" rx="1" fill="#d9d9d9"/><circle cx="6" cy="6" r="3.5" fill="none" stroke="#121212"/><path d="M2.5 6h7M6 2.5c-1.5 2-1.5 5 0 7M6 2.5c1.5 2 1.5 5 0 7" fill="none" stroke="#121212" stroke-width=".8"/></svg>
      </li>
    </ul>
  </section>
</body>
</html>
```